Growing Your Label eBook Cover Design

I want to deisgn a cover for my eBook (FRONT COVER) and the title is:

Why I Grew a Six-Figure Label. So You Should Start
By KL Baxter

TITLE CHANGED TO: OUT OF DEBT INTO POWER; WHY I GREW A NINE-FIGURE FORTUNE SO YOU SHOULD START

The color palette is attached. Along with some photos options of me. Along with the ebook in WORD Document. My website is www.KLBaXterHub.com. You can use a different color palette if you think it is best

Target Market(s)

women who look to build a personal brand

Industry/Entity Type

health and wellness

Requirements
Must have
• the title
Nice to have
• use my picture on the cover; but that is optional
Should not have
• any men

```html
<!DOCTYPE html>
<html lang="en">
<head>
<meta charset="UTF-8">
<title>Growing Your Label – eBook Cover</title>
<link href="https://fonts.googleapis.com/css2?family=Bebas+Neue&display=swap" rel="stylesheet">
<style>
  :root {
    --backdrop: #d2d4d6;
    --cover-ink: #060d16;
    --gold: #f5ab38;
    --white: #ffffff;
    --black: #0a0a0a;
    --teal-deep: #0f2a2a;
    --teal-mid: #1f4a45;
    --teal-light: #3c6b61;
  }
  html, body {
    margin: 0;
    padding: 0;
    width: 1117px;
    height: 1200px;
    overflow: hidden;
    background: var(--backdrop);
  }
  .canvas {
    display: block;
    width: 1117px;
    height: 1200px;
  }
  .title-text {
    font-family: "Bebas Neue", "Oswald", sans-serif;
  }
  .title-gold { fill: var(--gold); }
  .title-white { fill: var(--white); }
  .byline { fill: var(--black); font-family: "Bebas Neue", "Oswald", sans-serif; }
  .rule { stroke: var(--white); stroke-width: 2; }
</style>
</head>
<body>
<svg class="canvas" viewBox="0 0 1117 1200" xmlns="http://www.w3.org/2000/svg">
  <defs>
    <linearGradient id="sceneFade" x1="0" y1="0" x2="0" y2="1">
      <stop offset="0" stop-color="#060d16" stop-opacity="1"/>
      <stop offset="0.25" stop-color="#143230"/>
      <stop offset="0.6" stop-color="#1f4a45"/>
      <stop offset="0.85" stop-color="#6b6a48"/>
      <stop offset="1" stop-color="#1c3d38"/>
    </linearGradient>
  </defs>

  <g class="cover">
    <rect class="cover-base" x="228" y="103" width="661" height="992" fill="var(--cover-ink)"/>

    <rect class="cover-scene" x="228" y="664" width="661" height="362" fill="url(#sceneFade)"
          role="img" aria-label="Stacks of gold coins on a dark teal surface with rising financial chart lines behind them"/>

    <g class="title-text">
      <text class="title-gold" x="270" y="256.5" font-size="166" textLength="579" lengthAdjust="spacingAndGlyphs">WHY I GREW</text>

      <line class="rule" x1="270" y1="287" x2="539" y2="287"/>
      <text class="title-white" x="558.5" y="302" font-size="34" text-anchor="middle">A</text>
      <line class="rule" x1="578" y1="287" x2="848" y2="287"/>

      <text class="title-gold" x="270" y="401" font-size="118" textLength="577" lengthAdjust="spacingAndGlyphs">SIX-FIGURE</text>

      <text class="title-gold" x="270" y="629" font-size="298" textLength="576" lengthAdjust="spacingAndGlyphs">LABEL</text>

      <line class="rule" x1="270" y1="661" x2="525" y2="661"/>
      <text class="title-white" x="558.5" y="675" font-size="37" text-anchor="middle">SO</text>
      <line class="rule" x1="597" y1="661" x2="848" y2="661"/>

      <text class="title-white" x="270" y="772" font-size="109" textLength="578" lengthAdjust="spacingAndGlyphs">YOU SHOULD START</text>
    </g>

    <rect class="byline-band" x="228" y="1026" width="661" height="69" fill="var(--gold)"/>
    <text class="byline" x="558.5" y="1077" font-size="36" text-anchor="middle">BY KL BAXTER</text>
  </g>
</svg>
</body>
</html>
```